どのご提案もとても素敵で大変迷いましたが、こちらの作品が一番イメージにあっておりましたので採用させて頂きました。
皆さま、この度は素敵なご提案をありがとうございました!初めての利用で至らない点も多々あったかと思いますが、ご親切に対応頂き感謝しております。また機会がありましたら依頼させて頂きますので、その時はどうぞよろしくお願い致します。
ネイルサロンのバナーデザイン バナー作成・バナーデザインの仕事の依頼
大変失礼いたしました。
こちらはバナー制作ではなく、ヘッダー画像の制作をお願いしたいと思っております。
度々、追記を失礼します。
希望サイズですが記載の正方形ではなく
横1367に合わせた長方形でお願いします。
現在のウェブサイトはこんな感じです。
https://vemosquaril.com/
ターゲット層は30代後半〜50代。
料金価格設定は少し高めのサロンです。
使用していただきたいコピー候補は、
「デザインも大事だけどとにかくキレイに塗ってほしい」
「爪周りや爪の形など指全体を美しくしたい」
「爪のダメージ最小限で長く健康的にネイルを楽しみたい」
ネイルメロウジュは「本物の高いクオリティのネイル」を求める大人女性のためのネイルサロンです。
★ネイリスト全員が検定1級・コンテスト受賞も多数
★カウンセリング・アフターフォローも徹底重視
★はじめての方も大歓迎
この辺を使っていただきたいと考えております。
写真の候補はこちらの三枚です。

```html
<!DOCTYPE html>
<html lang="ja">
<head>
<meta charset="utf-8">
<title>ネイルメロウジュ岡山 ヘッダー</title>
<link href="https://fonts.googleapis.com/css2?family=Shippori+Mincho:wght@500;600;700&display=swap" rel="stylesheet">
<style>
  :root {
    --ink: #3a3533;
    --ink-soft: #5a5350;
    --panel: #ffffff;
    --panel-edge: #ececec;
    --gold-dark: #a9843d;
    --gold-light: #cfae6a;
    --photo-skin: #e9cfc4;
    --photo-skin-deep: #c99f90;
    --photo-light: #f4ebe6;
    --rule: #b9b2ae;
    --veil: rgba(255, 255, 255, 0.72);
  }
  * { margin: 0; padding: 0; box-sizing: border-box; }
  html, body { width: 1200px; height: 530px; overflow: hidden; background: var(--panel); }
  body { font-family: "Shippori Mincho", serif; color: var(--ink); }

  .header-banner { position: relative; width: 1200px; height: 530px; overflow: hidden; }

  .photo { position: absolute; top: 0; height: 530px; }
  .photo--left {
    left: 0; width: 330px;
    background: linear-gradient(160deg, var(--photo-light) 0%, var(--photo-skin) 45%, var(--photo-skin-deep) 100%);
  }
  .photo--right {
    right: 0; width: 330px;
    background: linear-gradient(200deg, var(--photo-skin-deep) 0%, var(--photo-skin) 40%, var(--photo-light) 100%);
  }

  .center-panel {
    position: absolute; left: 330px; top: 0; width: 540px; height: 530px;
    background: linear-gradient(90deg, var(--panel-edge) 0%, var(--panel) 12%, var(--panel) 88%, var(--panel-edge) 100%);
    text-align: center;
  }

  .lead, .headline, .sub, .points { position: absolute; left: 0; right: 0; white-space: nowrap; }
  .lead { top: 82px; font-size: 19px; font-weight: 600; letter-spacing: 0.08em; }
  .headline { top: 124px; font-size: 32px; line-height: 44px; font-weight: 700; letter-spacing: 0; }
  .headline__small { font-size: 25px; }
  .sub { top: 182px; font-size: 19px; font-weight: 600; letter-spacing: 0.08em; }

  .credential {
    position: absolute; top: 240px; left: 28px; width: 484px; height: 48px;
    background: linear-gradient(90deg, var(--gold-dark), var(--gold-light) 50%, var(--gold-dark));
    color: #fff; font-size: 17px; font-weight: 600; line-height: 44px; letter-spacing: 0.04em;
    border: 2px solid #fff; outline: 1px solid var(--gold-dark); white-space: nowrap;
  }
  .credential__strong { font-size: 20px; }

  .points { top: 322px; font-size: 19px; font-weight: 600; line-height: 36px; letter-spacing: 0.06em; color: var(--ink-soft); }

  .brand { position: absolute; top: 412px; left: 0; right: 0; }
  .brand__rule { display: block; margin: 0 auto; }
  .brand__name { display: block; margin-top: 14px; font-size: 28px; font-weight: 600; color: var(--ink); letter-spacing: 0.04em; }

  .vertical-copy {
    position: absolute; writing-mode: vertical-rl; font-weight: 600; color: var(--ink);
    white-space: nowrap; text-shadow: 0 0 6px var(--veil), 0 0 12px var(--veil);
  }
  .vertical-copy--left-a { top: 30px; left: 244px; font-size: 21px; letter-spacing: 0.1em; }
  .vertical-copy--left-b { top: 66px; left: 186px; font-size: 25px; letter-spacing: 0.12em; }
  .vertical-copy--right-a { top: 150px; left: 962px; font-size: 23px; letter-spacing: 0.1em; }
  .vertical-copy--right-b { top: 150px; left: 900px; font-size: 33px; letter-spacing: 0.04em; }
</style>
</head>
<body>
<section class="header-banner">
  <div class="photo photo--left" role="img" aria-label="ベージュ系のネイルを施した指先のクローズアップ写真"></div>
  <div class="photo photo--right" role="img" aria-label="ヌーディなグラデーションネイルの指先写真"></div>

  <p class="vertical-copy vertical-copy--left-a">爪のダメージを最小限に、</p>
  <p class="vertical-copy vertical-copy--left-b">長く健康的にネイルを楽しみたい</p>

  <div class="center-panel">
    <p class="lead">ネイルメロウジュ岡山は、派手さではなく</p>
    <h1 class="headline">「本物の高いクオリティ<span class="headline__small">の</span>ネイル」</h1>
    <p class="sub">を求める大人女性のためのネイルサロン</p>
    <p class="credential">ネイリスト全員が<span class="credential__strong">検定1級</span>＋コンテスト多数受賞</p>
    <p class="points">カウンセリング・アフターフォローも徹底重視<br>はじめての方も大歓迎！</p>
    <div class="brand">
      <svg class="brand__rule" width="300" height="2" viewBox="0 0 300 2" aria-hidden="true"><line x1="0" y1="1" x2="300" y2="1" stroke="var(--rule)" stroke-width="1"/></svg>
      <span class="brand__name">Nail Mellouge</span>
    </div>
  </div>

  <p class="vertical-copy vertical-copy--right-a">爪周りや爪の形など</p>
  <p class="vertical-copy vertical-copy--right-b">指全体を美しくしたい</p>
</section>
</body>
</html>
```